Halvering & Partners, LLC Business Card 2016

We need a new business card design for a very important trade show coming up.

We are a compliance Consulting Firm. Our clients are stock brokerage firms and investment advisers.

I would like our logo on both sides of the card.

Info in the front of the card shold include:

Logo
First & Last Name
Title
Office #
Cell #
Email
Company Address (42 W. Calloway Blvd., Suite 300 Pasadena, CA 91847

Back of the card should include the logo and url: www.halveringpartnersgroup.com

Target Market(s)

Stock Brokerage Firms and Investment Advisers

Industry/Entity Type

Financial Service

Contact Information for Business Card

Russell K. Halvering
President
42 W. Calloway Blvd., Suite 300
Pasadena, CA 91847
O 626.555.0147 ext. 204
C 818.555.0192
Email: russ@halveringpartnersgroup.com
www.halveringpartnersgroup.com

Requirements
Nice to have
• The back of the card could be black with the logo with the white letters.
• I do want the front of the card to at least have the color logo with the black "Halvering & Partners Lettering.

```html
<!DOCTYPE html>
<html lang="en">
<head>
<meta charset="utf-8">
<title>Halvering &amp; Partners, LLC — Business Card</title>
<link rel="stylesheet" href="https://fonts.googleapis.com/css2?family=EB+Garamond:ital,wght@0,400;0,500;1,400&display=swap">
<style>
  :root {
    --canvas: #e9e7e4;
    --card-dark: #262425;
    --card-white: #ffffff;
    --brand-red: #d83a2f;
    --ink-light: #f2f2f2;
    --ink-grey: #b9b9bb;
    --ink-black: #1d1c1d;
    --serif: "EB Garamond", Georgia, serif;
  }
  html, body {
    margin: 0;
    width: 1200px;
    height: 813px;
    overflow: hidden;
    background: var(--canvas);
    font-family: var(--serif);
  }
  .sheet {
    position: relative;
    width: 1200px;
    height: 813px;
    display: flex;
    align-items: center;
    justify-content: center;
    gap: 40px;
  }
  .card {
    position: relative;
    width: 540px;
    height: 309px;
    background: var(--card-dark);
    box-shadow: 0 6px 18px rgba(0,0,0,.25);
    overflow: hidden;
  }
  .card-shapes {
    position: absolute;
    inset: 0;
  }
  .brand-mark {
    position: absolute;
    display: flex;
    align-items: center;
    gap: 12px;
  }
  .brand-square {
    width: 26px;
    height: 26px;
    background: var(--brand-red);
    flex: none;
  }
  .brand-name {
    font-size: 22px;
    font-weight: 400;
    letter-spacing: 1.5px;
    text-transform: uppercase;
    line-height: 1;
  }
  /* front */
  .front .brand-mark { left: 30px; top: 132px; gap: 12px; }
  .front .brand-square { width: 34px; height: 34px; }
  .front .brand-name {
    color: var(--ink-black);
    font-size: 17px;
    line-height: 21px;
  }
  .front-company {
    position: absolute;
    right: 22px;
    top: 10px;
    color: var(--ink-grey);
    font-size: 18px;
    line-height: 22px;
    letter-spacing: 1.5px;
    text-align: right;
    text-transform: uppercase;
  }
  .holder {
    position: absolute;
    right: 22px;
    top: 66px;
    text-align: right;
  }
  .holder-name {
    color: var(--ink-light);
    font-size: 17px;
    letter-spacing: .8px;
    text-transform: uppercase;
  }
  .holder-title {
    color: var(--brand-red);
    font-size: 17px;
    font-style: italic;
    margin-top: -2px;
  }
  .contact-list {
    position: absolute;
    right: 22px;
    top: 132px;
    margin: 0;
    padding: 0;
    list-style: none;
    text-align: right;
  }
  .contact-list li {
    display: flex;
    align-items: center;
    justify-content: flex-end;
    gap: 8px;
    color: var(--ink-light);
    font-size: 14.5px;
    line-height: 25px;
  }
  .contact-icon {
    width: 15px;
    height: 15px;
    border-radius: 50%;
    background: var(--brand-red);
    display: flex;
    align-items: center;
    justify-content: center;
  }
  .address {
    position: absolute;
    right: 46px;
    bottom: 14px;
    text-align: right;
    color: var(--ink-light);
    font-size: 14.5px;
    line-height: 20px;
    font-style: normal;
  }
  /* back */
  .back .brand-mark { left: 62px; top: 112px; }
  .back .brand-square { width: 38px; height: 38px; }
  .back .brand-name { color: var(--ink-light); font-size: 27px; }
  .back-url {
    position: absolute;
    left: 0;
    right: 0;
    top: 214px;
    text-align: center;
    color: var(--ink-light);
    font-size: 17px;
    letter-spacing: .3px;
  }
  .back-url .url-core { color: var(--brand-red); }
</style>
</head>
<body>
<main class="sheet">

  <section class="card front" aria-label="Card front">
    <svg class="card-shapes" viewBox="0 0 540 309" aria-hidden="true">
      <polygon points="0,0 290,0 170,309 0,309" fill="var(--card-white)"/>
      <polygon points="201,230 540,230 540,309 170,309" fill="var(--brand-red)"/>
      <polygon points="302,0 314,0 289,64 277,64" fill="var(--brand-red)"/>
      <rect x="289" y="61" width="150" height="3" fill="var(--brand-red)"/>
    </svg>

    <div class="brand-mark">
      <span class="brand-square"></span>
      <span class="brand-name">Halvering<br>&amp; Partners</span>
    </div>

    <div class="front-company">Halvering<br>&amp; Partners</div>

    <div class="holder">
      <div class="holder-name">Russell K. Halvering</div>
      <div class="holder-title">President</div>
    </div>

    <ul class="contact-list">
      <li>626.555.0147 ext. 204
        <span class="contact-icon"><svg width="9" height="9" viewBox="0 0 10 10"><path d="M2 1l2 2-1 1.2c.6 1.2 1.6 2.2 2.8 2.8L7 6l2 2-1.2 1.4C4.5 9.2.8 5.5.6 2.2z" fill="#fff"/></svg></span>
      </li>
      <li>818.555.0192
        <span class="contact-icon"><svg width="9" height="9" viewBox="0 0 10 10"><rect x="2.5" y="0.5" width="5" height="9" rx="1" fill="none" stroke="#fff" stroke-width="1.2"/><circle cx="5" cy="7.8" r=".6" fill="#fff"/></svg></span>
      </li>
      <li>russ@halveringpartnersgroup.com
        <span class="contact-icon"><svg width="9" height="9" viewBox="0 0 10 10"><rect x="0.8" y="2" width="8.4" height="6" fill="none" stroke="#fff" stroke-width="1.1"/><path d="M1 2.3l4 3 4-3" fill="none" stroke="#fff" stroke-width="1.1"/></svg></span>
      </li>
    </ul>

    <address class="address">
      42 W. Calloway Blvd., Suite 300<br>
      Pasadena, CA 91847
    </address>
  </section>

  <section class="card back" aria-label="Card back">
    <div class="brand-mark">
      <span class="brand-square"></span>
      <span class="brand-name">Halvering &amp; Partners</span>
    </div>
    <div class="back-url">www.<span class="url-core">halveringpartnersgroup</span>.com</div>
  </section>

</main>
</body>
</html>
```